High Quality Flyer Design For Real Estate Website

I require a double sided flyer for the website tallowbrookhomes.net.

The flyer size should be A5.

The flyer must be fresh and up to date and go with the theme of the website.
Updates

Old flyer attachment was missing, but is now attached.

Target Market(s)

Landlords and people looking to buy or sell their house of all age groups

Industry/Entity Type

Real Estate

Font styles to use
Sans Serif

Requirements
Must have
• The main colour of the flyer should be the yellow used on the website.

The logo from the website should also be used (attached)

The text included on the old flyer must be on the new flyer (see attachment)

The flyer should take the reader through a process (see old attached flyer) and make them feel that using the website is very simple.

Nice to have

```html
<!DOCTYPE html>
<html lang="en">
<head>
<meta charset="utf-8">
<title>Tallowbrook Homes – Flyer</title>
<link rel="stylesheet" href="https://fonts.googleapis.com/css2?family=Carlito:wght@400;700&display=swap">
<style>
  :root {
    --brand-yellow: #fdc200;
    --ink: #000000;
    --paper: #ffffff;
    --panel-grey: #eeeeee;
    --icon-grey: #777777;
    --circle-grey: #e6e6e6;
    --shadow: rgba(0,0,0,0.45);
  }
  * { margin: 0; padding: 0; box-sizing: border-box; }
  html, body { width: 1200px; height: 846px; overflow: hidden; background: var(--paper); }
  body { font-family: "Carlito", "Calibri", sans-serif; color: var(--ink); }

  .flyer { position: relative; width: 1200px; height: 846px; overflow: hidden; background: var(--paper); }
  .flyer__yellow-half { position: absolute; left: 0; top: 0; width: 612px; height: 786px; background: var(--brand-yellow); }

  .headline {
    position: absolute; left: 20px; top: 46px; width: 572px;
    font-size: 41px; line-height: 60px; text-align: center; font-weight: 400;
  }

  /* Website preview */
  .site-preview {
    position: absolute; left: 642px; top: 30px; width: 490px; height: 306px;
    background: var(--panel-grey); overflow: hidden;
    box-shadow: 4px 5px 6px var(--shadow);
  }
  .site-preview__header { position: absolute; left: 0; top: 0; width: 100%; height: 42px; background: var(--ink); }
  .site-preview__logo { position: absolute; left: 44px; top: 8px; display: flex; align-items: center; gap: 5px; }
  .site-preview__logo-mark { width: 12px; height: 12px; background: var(--brand-yellow); }
  .site-preview__logo-name { color: var(--brand-yellow); font-size: 14px; font-weight: 700; }
  .site-preview__tagline { position: absolute; left: 44px; top: 27px; color: var(--brand-yellow); font-size: 5px; }
  .site-preview__email { position: absolute; right: 44px; top: 14px; color: var(--paper); font-size: 7px; }
  .site-preview__nav {
    position: absolute; left: 0; top: 42px; width: 100%; height: 24px; background: var(--brand-yellow);
    display: flex; align-items: center; padding-left: 42px; gap: 0; font-size: 6.5px; color: var(--ink);
  }
  .site-preview__nav span { padding: 0 6px; line-height: 18px; }
  .site-preview__nav .is-active { background: var(--ink); color: var(--paper); }

  .site-preview__hero {
    position: absolute; left: 42px; top: 78px; width: 294px; height: 122px;
    background: linear-gradient(135deg, #2b2b2b 0%, #6a5a3a 45%, #c9a96a 75%, #3a3a3a 100%);
  }
  .hero-tag {
    position: absolute; left: 6px; font-size: 6.5px; color: var(--brand-yellow);
    border: 1px solid var(--brand-yellow); padding: 1px 4px; background: rgba(0,0,0,0.35);
  }

  .site-preview__search {
    position: absolute; left: 348px; top: 78px; width: 90px; height: 122px;
    background: var(--brand-yellow); padding: 4px 5px; font-size: 5px;
  }
  .search-row { display: flex; gap: 8px; margin-bottom: 4px; }
  .search-field { background: var(--paper); height: 7px; margin: 1px 0 3px; }
  .search-pair { display: flex; gap: 4px; }
  .search-pair > div { flex: 1; }
  .search-button { background: var(--ink); color: var(--paper); text-align: center; font-size: 6px; line-height: 10px; margin-top: 2px; }

  .site-preview__features {
    position: absolute; left: 42px; top: 210px; width: 396px; height: 96px; background: var(--paper);
  }
  .feature { position: absolute; top: 6px; width: 120px; text-align: center; }
  .feature__icon { width: 46px; height: 46px; border-radius: 50%; background: var(--circle-grey); margin: 0 auto; display: flex; align-items: center; justify-content: center; }
  .feature__label { display: inline-block; margin-top: 8px; background: var(--ink); color: var(--brand-yellow); font-size: 7px; padding: 2px 4px; }
  .feature__caption { font-size: 4.5px; color: #555; margin-top: 3px; }

  /* Steps */
  .steps {
    position: absolute; left: 48px; top: 394px; width: 1102px; height: 268px; background: var(--ink);
    display: grid; grid-template-columns: 364px 367px 371px;
  }
  .step { position: relative; text-align: center; color: var(--brand-yellow); }
  .step + .step::before {
    content: ""; position: absolute; left: 0; top: 32px; width: 3px; height: 216px; background: var(--brand-yellow);
  }
  .step__number { position: absolute; left: 0; right: 0; top: 22px; font-size: 31px; }
  .step__text { position: absolute; left: 6px; right: 6px; top: 124px; font-size: 34px; line-height: 40px; }

  .closing {
    position: absolute; left: 0; top: 683px; width: 1200px; text-align: center;
    font-size: 26px; line-height: 39px;
  }
  .footer-band {
    position: absolute; left: 0; top: 786px; width: 1200px; height: 60px; background: var(--ink);
    color: var(--paper); font-size: 38px; text-align: center; line-height: 60px;
  }
</style>
</head>
<body>
<main class="flyer">
  <div class="flyer__yellow-half"></div>

  <h1 class="headline">For a limited time only, we are offering you the opportunity to use our NEW WEBSITE for FREE to Buy, Sell or Let your next property.</h1>

  <section class="site-preview" aria-label="Website homepage preview">
    <div class="site-preview__header">
      <div class="site-preview__logo"><span class="site-preview__logo-mark"></span><span class="site-preview__logo-name">tallowbrookhomes.net</span></div>
      <div class="site-preview__tagline">Sell and let property without fees</div>
      <div class="site-preview__email">✉ info@tallowbrookhomes.net</div>
    </div>
    <nav class="site-preview__nav">
      <span class="is-active">Home</span><span>For Sale</span><span>For Rent</span><span>Sell Or Let</span><span>Property Value</span><span>Guide ▾</span><span>Blog</span><span>Contact Us</span><span>Log In</span><span>Register</span>
    </nav>

    <div class="site-preview__hero" role="img" aria-label="Photo of one hand passing a small model house into another open hand">
      <span class="hero-tag" style="top:50px">SELL OR RENT YOUR PROPERTY</span>
      <span class="hero-tag" style="top:72px;left:22px">COMMISSION FREE</span>
      <span class="hero-tag" style="top:94px">&amp; SAY HELLO TO TALLOWBROOK</span>
    </div>

    <div class="site-preview__search">
      <div class="search-row"><span>○ For Sale</span><span>● For Rent</span></div>
      <div>Location</div><div class="search-field"></div>
      <div>Type</div><div class="search-field"></div>
      <div class="search-pair"><div>Beds<div class="search-field"></div></div><div>Baths<div class="search-field"></div></div></div>
      <div class="search-pair"><div>Price From<div class="search-field"></div></div><div>Price To<div class="search-field"></div></div></div>
      <div class="search-button">Search</div>
    </div>

    <div class="site-preview__features">
      <div class="feature" style="left:2px">
        <div class="feature__icon">
          <svg width="20" height="20" viewBox="0 0 20 20"><path d="M10 2 L19 10 H16 V18 H12 V13 H8 V18 H4 V10 H1 Z" fill="var(--icon-grey)"/></svg>
        </div>
        <span class="feature__label">Properties For Sale</span>
        <div class="feature__caption">Find the latest properties for sale</div>
      </div>
      <div class="feature" style="left:140px">
        <div class="feature__icon">
          <svg width="24" height="14" viewBox="0 0 24 14"><circle cx="6" cy="7" r="5" fill="none" stroke="var(--icon-grey)" stroke-width="2.5"/><path d="M11 7 H23 M18 7 V11 M22 7 V10" stroke="var(--icon-grey)" stroke-width="2.5" fill="none"/></svg>
        </div>
        <span class="feature__label">Properties For Rent</span>
        <div class="feature__caption">Search the latest properties to rent</div>
      </div>
      <div class="feature" style="left:274px">
        <div class="feature__icon">
          <svg width="20" height="20" viewBox="0 0 20 20"><rect x="2" y="4" width="14" height="14" fill="none" stroke="var(--icon-grey)" stroke-width="2"/><path d="M5 10 L9 14 L18 3" fill="none" stroke="var(--icon-grey)" stroke-width="2.5"/></svg>
        </div>
        <span class="feature__label">Submit Your Property</span>
        <div class="feature__caption">Sell or let your property free</div>
      </div>
    </div>
  </section>

  <section class="steps">
    <div class="step"><div class="step__number">Step 1</div><div class="step__text">Go to<br>tallowbrookhomes.net</div></div>
    <div class="step"><div class="step__number">Step 2</div><div class="step__text">Create an account</div></div>
    <div class="step"><div class="step__number">Step 3</div><div class="step__text">Upload your property using the simple step by step process</div></div>
  </section>

  <p class="closing">Once your property is uploaded, any interested Buyers and Tenants can contact you<br>directly, to negotiate a price SAVING You £1000’s in Estate Agent Fees</p>

  <footer class="footer-band">www.tallowbrookhomes.net</footer>
</main>
</body>
</html>
```